Tarnabee Wines - web page for new Australian wine label

We need a landing page for our wine company. Tarnabee is a family owned company, we grow the gapes, and make the wine in the Clare valley. Daniel Hovsted is the winemaker and is well known for his style, which is all about the fruit flavour rather than wood or age influences. Tarnabee is Abriginal for 2 hills and a water source. We hand pick, hand plunge, foot crush resulting in elegant wine. Little to no additives, minimal filtering, single vineyard wines. Handcrafted with small releases of only the best fruit from carefully selected rows and bunches. The Clare valley is located two hours North of Adelaide, is known for cool climate and slow ripening, resulting in wines that have an elegant mouth feel, with bright colour and outstanding flavours. Our Sevenhill vineyard has a Eastern aspect, gathering morning sun and escaping the hot afternoons, and in our opinion is on of the prettiest valleys in the world. Only 1000 cases per annum of the very best handpicked fruit, from the best rows. We hope you enjoy the Tarnabee style, the reds are lighter in colour, fruit driven palate, more old world influence and the Riesling is on the dry side with fresh citrus. Minimal additives and filtering, our aim was to make wine with minimal influence from wine making. Handcrafted wines.

Target Market(s)

females 18 - 60 are the ones that buy 70 percent of wine, so whilst men are also a target, its the ladies we seek to appeal to.

Industry/Entity Type

It Company

Number of Pages Required

4 page

Font styles to use
Serif

Requirements
Must have
• Eye catching front page that makes me feel like i am ordering from quality company, that cares for what they do. Easy to use ordering, and delivery instructions.
• postage is $14.90 per case Australia wide.
• www.tarnabeewines.com
Nice to have
• I want to see a fun and family oriented business that cares for the wine, we dont make a lot, its buckets and feet. But its wine made wanting to be the best in the world, we dont cut corners on quality. Handcrafted
Should not have
• dont really have any thoughts here, looking for all ideas

```html
<!DOCTYPE html>
<html lang="en">
<head>
<meta charset="utf-8">
<title>Tarnabee Wines</title>
<link rel="stylesheet" href="https://fonts.googleapis.com/css2?family=Caveat+Brush&family=Merriweather:ital,wght@0,400;0,700;1,400&display=swap">
<style>
:root{
  --blue:#1f62b3;
  --blue-deep:#0f4a9a;
  --pink:#c784b2;
  --ink:#555;
  --ink-dark:#333;
  --paper:#fbfbf9;
  --footer-a:#7ea3de;
  --footer-b:#4f7fcf;
  --white:#fff;
}
*{box-sizing:border-box;margin:0;padding:0}
html,body{width:1200px;height:4675px;overflow:hidden}
body{position:relative;background:var(--paper);font-family:"Merriweather",Georgia,serif;color:var(--ink)}
.abs{position:absolute}
.brand{font-family:"Merriweather",Georgia,serif;font-weight:400;font-size:46px;color:var(--pink);left:60px;top:40px;letter-spacing:1px}
.menu{right:42px;top:60px;width:56px}
.menu span{display:block;height:7px;background:var(--blue-deep);border-radius:4px;margin-bottom:10px}
.hero-visual{left:590px;top:30px;width:600px;height:730px;border-radius:46% 38% 42% 50%/40% 46% 44% 50%;
  background:radial-gradient(ellipse at 70% 55%,#5a6d7a 0 12%,transparent 30%),radial-gradient(ellipse at 35% 70%,#b8443a 0 10%,transparent 28%),linear-gradient(180deg,#cfe0ea,#e7ebe8 45%,#d9d4c6);opacity:.9}
.hero-title{left:84px;top:150px;font-family:"Caveat Brush",cursive;color:var(--blue);font-size:148px;line-height:128px;transform:rotate(-4deg);transform-origin:left top}
.shop-btn{left:134px;top:655px;width:366px;height:62px;border-radius:31px;background:var(--pink);color:var(--white);font-family:Arial,Helvetica,sans-serif;font-weight:700;font-size:36px;letter-spacing:2px;text-align:center;line-height:62px}
.intro{left:140px;top:808px;width:930px;font-weight:700;font-size:25px;line-height:36px;color:var(--ink)}
.copy{font-size:17px;line-height:31px;color:var(--ink)}
.copy p+p{margin-top:20px}
.photo{border-radius:40% 30% 36% 44%/30% 40% 34% 40%}
.photo-team{left:655px;top:997px;width:451px;height:343px;background:linear-gradient(160deg,#8a7a63,#3e3a36 60%,#6b5d4b)}
.photo-grapes{left:140px;top:1418px;width:437px;height:312px;background:linear-gradient(150deg,#c8b4ad,#4d3447 55%,#8f6f7a)}
.band{left:0;top:1840px;width:1200px;height:750px;background:linear-gradient(180deg,#9aa58a,#6f7f54 35%,#7d5e3c 70%,#c9b9a3);border-radius:8% 6% 10% 8%/12% 10% 14% 12%}
.band-quote{left:0;top:2125px;width:1200px;text-align:center;font-family:"Caveat Brush",cursive;color:var(--white);font-size:66px;line-height:72px}
.range-title{left:0;top:2650px;width:1200px;text-align:center;font-family:"Caveat Brush",cursive;color:var(--blue);font-size:90px}
.range{left:150px;top:2820px;width:900px;display:flex;justify-content:space-between}
.wine{width:170px;text-align:center}
.wine-bottle{margin:0 auto;width:74px;height:300px;border-radius:26px 26px 8px 8px;background:linear-gradient(90deg,#9a9a9a,#c4c4c4 40%,#8c8c8c)}
.wine-bottle.active{background:linear-gradient(90deg,#7d9a2e,#c4dc68 40%,#6d8a24)}
.wine-name{margin-top:10px;font-size:14px;font-weight:700;line-height:18px;color:var(--ink-dark)}
.feature-bottle{left:225px;top:3270px;width:190px;height:660px;border-radius:60px 60px 14px 14px;background:linear-gradient(90deg,#6f8d24,#cfe27a 40%,#5f7c1c)}
.feature-brand{left:610px;top:3318px;font-size:40px;color:var(--blue)}
.feature-vintage{left:650px;top:3378px;font-size:20px;color:var(--blue);font-variant:small-caps}
.feature-desc{left:560px;top:3412px;width:370px;font-size:13px;line-height:25px;color:var(--ink-dark)}
.scale{left:628px;top:3608px;width:288px}
.scale-bar{display:flex;height:8px;border:1px solid #777}
.scale-bar i{flex:1;border-right:1px solid #777}
.scale-bar i:first-child{background:var(--blue)}
.scale-labels{display:flex;justify-content:space-between;font-size:7px;color:#777;margin-top:2px}
.price{left:560px;top:3688px;font-size:48px;color:var(--ink)}
.price small{font-size:18px}
.qty{left:560px;top:3778px;width:66px;height:50px;border:2px solid #999;font-size:18px;text-align:center;line-height:46px;color:var(--ink-dark);background:var(--white)}
.trolley{left:655px;top:3780px;width:228px;height:48px;background:var(--pink);color:var(--white);font-family:Arial,Helvetica,sans-serif;font-weight:700;font-size:16px;letter-spacing:1px;text-align:center;line-height:48px}
.footer{left:0;top:3950px;width:1200px;height:725px;background:linear-gradient(170deg,var(--footer-a),var(--footer-b) 60%,#8fb0e2)}
.footer-art{left:690px;top:4020px;width:480px;height:600px;border-radius:50% 40% 40% 50%;background:radial-gradient(ellipse at 60% 50%,rgba(255,255,255,.65),rgba(180,210,160,.45) 55%,transparent 75%)}
.footer-brand{left:44px;top:4030px;font-size:52px;color:var(--white)}
.footer-h{font-size:34px;font-weight:700;color:var(--white)}
.contact{left:44px;top:4170px;font-size:28px;color:var(--white)}
.contact li{list-style:none;display:flex;align-items:center;gap:22px;height:62px}
.contact svg{width:32px;height:32px;fill:var(--white)}
.email-field{left:37px;top:4408px;width:400px;height:44px;border-radius:22px;background:var(--white);font-size:18px;color:#999;padding-left:26px;line-height:44px;letter-spacing:1px}
.email-field svg{position:absolute;right:22px;top:10px;width:34px;height:24px}
.social{left:44px;top:4540px;display:flex;gap:14px}
.social i{display:block;width:42px;height:42px;border-radius:50%;background:var(--white)}
.legal{left:0;top:4628px;width:1200px;height:47px;background:var(--white);display:flex;justify-content:space-between;align-items:center;padding:0 30px 0 55px;font-size:14px;color:var(--ink-dark)}
</style>
</head>
<body>
<header>
  <div class="abs brand">Tarnabee</div>
  <div class="abs menu" aria-label="Menu"><span></span><span></span><span></span></div>
</header>

<section class="hero">
  <div class="abs hero-visual" role="img" aria-label="Watercolour scene of a white wine bottle with a red lobster on a beach"></div>
  <h1 class="abs hero-title">Elegant<br>hand-crafted<br>wines</h1>
  <div class="abs shop-btn">SHOP NOW</div>
</section>

<section class="about">
  <p class="abs intro">Tarnabee is a family owned company, we grow the grapes, and make the wine in the Clare valley. Daniel Hovsted is the winemaker and is well known for his style, which is all about the fruit flavour rather than wood or age influences.</p>
  <div class="abs copy" style="left:140px;top:980px;width:470px">
    <p>Tarnabee is Aboriginal for 2 hills and a water source. We hand pick, hand plunge, foot crush resulting in elegant wine. Little to no additives, minimal filtering, single vineyard wines. Handcrafted with small releases of only the best fruit from carefully selected rows and bunches.</p>
    <p>The Clare valley is located two hours North of Adelaide, is known for cool climate and slow ripening, resulting in wines that have an elegant mouth feel, with bright colour and outstanding flavours.</p>
  </div>
  <div class="abs photo photo-team" role="img" aria-label="Photo of the winemakers among barrels in the cellar"></div>
  <div class="abs photo photo-grapes" role="img" aria-label="Photo of feet crushing red grapes"></div>
  <div class="abs copy" style="left:648px;top:1418px;width:460px">
    <p>Our Sevenhill vineyard has a Eastern aspect, gathering morning sun and escaping the hot afternoons, and in our opinion is on of the prettiest valleys in the world.</p>
    <p>We hope you enjoy the Tarnabee style, the reds are lighter in colour, fruit driven palate, more old world influence and the Riesling is on the dry side with fresh citrus. Minimal additives and filtering, our aim was to make wine with minimal influence from wine making. Handcrafted wines.</p>
  </div>
</section>

<section class="harvest">
  <div class="abs band" role="img" aria-label="Photo of a grape picker holding a bunch among the vines"></div>
  <p class="abs band-quote">Only 1000 cases per annum<br>of the very best handpicked fruit,<br>from the best rows.</p>
</section>

<section class="shop">
  <h2 class="abs range-title">Our range</h2>
  <div class="abs range">
    <div class="wine"><div class="wine-bottle" role="img" aria-label="Bottle"></div><p class="wine-name">2016 Shiraz Cabernet Sauvignon Clare Valley</p></div>
    <div class="wine"><div class="wine-bottle active" role="img" aria-label="Bottle"></div><p class="wine-name">2016 Riesling Clare Valley</p></div>
    <div class="wine"><div class="wine-bottle" role="img" aria-label="Bottle"></div><p class="wine-name">2016 Reserve Cabernet Sauvignon Single Vineyard Sevenhill</p></div>
    <div class="wine"><div class="wine-bottle" role="img" aria-label="Bottle"></div><p class="wine-name">2016 Shiraz Clare Valley</p></div>
    <div class="wine"><div class="wine-bottle" role="img" aria-label="Bottle"></div><p class="wine-name">2016 Reserve Shiraz Single Vineyard Sevenhill Clare Valley</p></div>
  </div>

  <div class="abs feature-bottle" role="img" aria-label="Bottle of 2016 Riesling"></div>
  <div class="abs feature-brand">Tarnabee</div>
  <div class="abs feature-vintage">2016 Riesling</div>
  <p class="abs feature-desc">This dry Riesling is from a single vineyard on the North-Eastern ridge of the Clare Valley. Juicy tropical fruits are followed by lovely lime and lemon zest characters, which gives the wine great vibrancy and refreshing length. 250 Dozen produced. Drink 2016 – 2025.</p>
  <div class="abs scale">
    <div class="scale-bar"><i></i><i></i><i></i><i></i></div>
    <div class="scale-labels"><span>Dry</span><span>Off-dry</span><span>Medium</span><span>Sweet</span></div>
  </div>
  <p class="abs price">A$39.99 <small>per case</small></p>
  <div class="abs qty">1</div>
  <div class="abs trolley">ADD TO TROLLEY</div>
</section>

<footer>
  <div class="abs footer"></div>
  <div class="abs footer-art" role="img" aria-label="Watercolour illustration of lily of the valley flowers"></div>
  <div class="abs footer-brand">Tarnabee</div>
  <h3 class="abs footer-h" style="left:44px;top:4105px">Contact details</h3>
  <ul class="abs contact">
    <li><svg viewBox="0 0 24 24"><path d="M12 2a7 7 0 0 0-7 7c0 5 7 13 7 13s7-8 7-13a7 7 0 0 0-7-7zm0 9.5A2.5 2.5 0 1 1 12 6.5a2.5 2.5 0 0 1 0 5z"/></svg>Tarnabee HQ, Clare Valley, Australia</li>
    <li><svg viewBox="0 0 24 24"><path d="M6.6 10.8a15 15 0 0 0 6.6 6.6l2.2-2.2a1 1 0 0 1 1-.25 11.4 11.4 0 0 0 3.6.57 1 1 0 0 1 1 1V20a1 1 0 0 1-1 1A17 17 0 0 1 3 4a1 1 0 0 1 1-1h3.5a1 1 0 0 1 1 1c0 1.25.2 2.45.57 3.6a1 1 0 0 1-.25 1z"/></svg>08 8842 1107</li>
    <li><svg viewBox="0 0 24 24"><path d="M2 5h20v14H2zm2 2v.5l8 5 8-5V7zm0 2.8V17h16V9.8l-8 5z"/></svg>info@tarnabee.com</li>
  </ul>
  <h3 class="abs footer-h" style="left:44px;top:4348px">Newsletter</h3>
  <div class="abs email-field">EMAIL<svg viewBox="0 0 34 24"><rect x="1" y="1" width="32" height="22" fill="none" stroke="#4f7fcf" stroke-width="2"/><path d="M1 1l16 12L33 1" fill="none" stroke="#4f7fcf" stroke-width="2"/></svg></div>
  <h3 class="abs footer-h" style="left:44px;top:4478px">Follow us</h3>
  <div class="abs social" aria-label="Social links"><i></i><i></i><i></i><i></i></div>
  <div class="abs legal"><span>Legal information | Terms | Data Privacy | Shipping | Contact</span><span>© Tarnabee 2017. All Rights Reserved!</span></div>
</footer>
</body>
</html>
```